Newly created Management Consulting company needs a brochure to capture clients's interest

This is a new management consulting firm providing service in Finance, Marketing, Operations/Manufacturing Strategy, and Project Management.
Please go to the company's website: www.veltanorpartners.ca . The website is pretty straightforward and gives a clear explanation of all the services and sub-services offered. Based on the existent material on the website, I would like to create a company's brochure that can inspire clients to seek our services.
One important thing: the slogan/tagline ("Shaping the future of your business") needs to be added somewhere in the vicinity of our company's' LOGO. Please see attached the company's logo (JPEG file).
The brochure size and number of pages can vary, depending on the layout of the brochure so it can fit the content, so I am open to different and innovative sizes/shapes and no. of pages etc. Graphics should combine real pictures with graphic design technology, and should give a professional look and feel comparable to big companies' marketing materials.
Updates
The brochure does not necessarily have to include pictures that are on the website. If you think that other pictures and graphics can deliver a stronger message to customers, by all means I am open to any other ideas.
Thanks.
As I said before, the pictures do not need to be exactly the same pictures as on the website, if you can bring in other cool pictures to attract clients, please go ahead. Also, you do not need to use only black background, if you have better colors ideas to combine with the our LOGO, and it looks good, by all means do use other colors. But our LOGO needs to be represented as it is on the JPEG I attached.
May the most creative and cool design win! Good luck!
Please ensure that all the content of our website fits into your brochure, including our contact information. It is up to you to come up with the necessary number of pages, design and shape of the brochure, but the text should be clear enough to be read by a normal person without a magnifying glass.
Thank you.
In order to keep the brochure to a reasonable number of pages, I agree that it is not necessary to include 100% all the text that appears on the website. That being said, even if you do not have enough space to include all the background and introduction paragraphs under each service/sub-service, it is still important that the main message for each service/sub-service is being contained in the brochure.
Target Market(s)
Our clients are companies with sizes starting from 10-20 employees and up to large Larkspan 700 companies.
Industry/Entity Type
Management Consulting
Look and feel

```html
<!DOCTYPE html>
<html lang="en">
<head>
<meta charset="utf-8">
<title>Veltanor Partners – Brochure</title>
<link rel="stylesheet" href="https://fonts.googleapis.com/css2?family=Roboto+Condensed:wght@400;700&family=Arimo:ital,wght@0,400;0,700;1,700&display=swap">
<style>
  :root {
    --backdrop: #e9e7e3;
    --ink-black: #050505;
    --panel-dark: #1f1f1f;
    --panel-mid: #262626;
    --brand-green: #5ea935;
    --text-light: #e6e6e6;
    --text-white: #ffffff;
    --photo-light: #d9d9d9;
    --photo-dark: #8a8a8a;
  }
  * { box-sizing: border-box; margin: 0; padding: 0; }
  html, body { width: 1200px; height: 626px; overflow: hidden; }
  body { background: var(--backdrop); font-family: "Arimo", Arial, sans-serif; }

  .brochure-spread {
    position: absolute; left: 218px; top: 29px;
    width: 764px; height: 568px;
    background: var(--panel-dark);
    box-shadow: 0 6px 18px rgba(0,0,0,.25);
    overflow: hidden;
  }

  /* inside spread: top photo across left two panels */
  .office-photo {
    position: absolute; left: 0; top: 0; width: 532px; height: 250px;
    background: linear-gradient(135deg, var(--photo-light) 0%, #bdbdbd 45%, var(--photo-dark) 100%);
  }
  .services-tab {
    position: absolute; left: 0; top: 209px; width: 185px; height: 41px;
    background: var(--brand-green);
    color: var(--text-white);
    font: 700 27px/41px "Roboto Condensed", "Arial Narrow", sans-serif;
    padding-left: 15px;
  }
  .services-rule {
    position: absolute; left: 185px; top: 246px; width: 347px; height: 4px;
    background: var(--brand-green);
  }

  /* left inner panel */
  .services-panel {
    position: absolute; left: 0; top: 250px; width: 267px; height: 318px;
    background: var(--panel-mid);
    padding: 22px 16px 0 18px;
  }
  .services-intro {
    color: var(--text-light); font-size: 9.6px; line-height: 13.2px;
    text-align: justify;
  }
  .services-intro .company-name { color: var(--brand-green); font-weight: 700; font-style: italic; }
  .services-list { list-style: none; margin-top: 18px; }
  .services-list li {
    color: var(--brand-green);
    font: 700 20px/36px "Roboto Condensed", "Arial Narrow", sans-serif;
    display: flex; align-items: center; gap: 6px;
  }
  .services-list svg { width: 16px; height: 14px; flex: none; }

  /* middle panel */
  .contact-panel {
    position: absolute; left: 267px; top: 250px; width: 265px; height: 318px;
    background: var(--panel-dark);
    text-align: center;
  }
  .contact-heading {
    color: var(--brand-green);
    font: 700 18px/1 "Roboto Condensed", "Arial Narrow", sans-serif;
    margin-top: 14px;
  }
  .contact-address { color: var(--text-light); font-size: 9.8px; line-height: 13.4px; margin-top: 10px; }
  .contact-phones {
    color: var(--brand-green);
    font: 700 17px/23px "Roboto Condensed", "Arial Narrow", sans-serif;
    margin-top: 12px;
  }
  .contact-email {
    color: var(--text-white);
    font: 700 15.5px/1.3 "Roboto Condensed", "Arial Narrow", sans-serif;
  }
  .skyline-photo {
    position: absolute; left: 0; bottom: 0; width: 265px; height: 120px;
    background: linear-gradient(180deg, var(--panel-dark) 0%, #3a3a3a 55%, #4b4b4b 100%);
  }
  .skyline-name {
    position: absolute; left: 0; right: 0; top: 34px;
    color: var(--text-white); font: 400 13px/1 "Roboto Condensed", "Arial Narrow", sans-serif;
    letter-spacing: 1px;
  }
  .social-row {
    position: absolute; left: 0; right: 0; bottom: 20px;
    display: flex; justify-content: center; align-items: center; gap: 5px;
    color: var(--brand-green); font: 700 11px/1 "Roboto Condensed", "Arial Narrow", sans-serif;
  }
  .social-row .social-label { margin-right: 4px; }
  .social-square { width: 15px; height: 15px; background: #6b6b6b; border-radius: 2px; }

  /* cover panel */
  .cover-panel {
    position: absolute; left: 532px; top: 0; width: 232px; height: 568px;
    background: var(--panel-dark);
  }
  .cover-top {
    position: absolute; left: 0; top: 0; width: 232px; height: 250px;
    background: var(--ink-black);
  }
  .cover-brand {
    position: absolute; left: 0; right: 0; top: 98px;
    text-align: center; color: var(--text-white);
    font: 400 34px/1.05 "Roboto Condensed", "Arial Narrow", sans-serif;
    letter-spacing: 1px;
  }
  .cover-tagline {
    position: absolute; left: 16px; top: 327px; right: 8px;
    font-family: "Roboto Condensed", "Arial Narrow", sans-serif; font-weight: 700;
  }
  .cover-tagline .tagline-lead {
    display: block; color: var(--brand-green);
    font-size: 49px; line-height: 52px; letter-spacing: -0.5px;
  }
  .cover-tagline .tagline-tail {
    display: block; color: var(--text-white);
    font-size: 28px; line-height: 36px; font-weight: 400;
  }
  .cover-url {
    position: absolute; left: 16px; bottom: 28px;
    color: var(--brand-green);
    font: 700 17px/1 "Roboto Condensed", "Arial Narrow", sans-serif;
  }
</style>
</head>
<body>
  <main class="brochure-spread">
    <div class="office-photo" role="img" aria-label="Black and white photo of a business meeting table with a laptop, papers and a coffee cup"></div>
    <h2 class="services-tab">Our Services</h2>
    <div class="services-rule"></div>

    <section class="services-panel">
      <p class="services-intro"><span class="company-name">Veltanor Partners</span> chief focus is addressing the critical business challenges of our clients. We work across all industries and guide our customers in making the right decisions and conducting the best course of action in operations, marketing, and finance. We come up with solutions for a company that will improve performance, reduce costs and maximize growth.</p>
      <ul class="services-list">
        <li><svg viewBox="0 0 16 14" aria-hidden="true"><path d="M1 1 L15 7 L1 13 L5 7 Z" fill="var(--brand-green)"/></svg>Finance</li>
        <li><svg viewBox="0 0 16 14" aria-hidden="true"><path d="M1 1 L15 7 L1 13 L5 7 Z" fill="var(--brand-green)"/></svg>Marketing</li>
        <li><svg viewBox="0 0 16 14" aria-hidden="true"><path d="M1 1 L15 7 L1 13 L5 7 Z" fill="var(--brand-green)"/></svg>Operations</li>
        <li><svg viewBox="0 0 16 14" aria-hidden="true"><path d="M1 1 L15 7 L1 13 L5 7 Z" fill="var(--brand-green)"/></svg>Project Management</li>
      </ul>
    </section>

    <section class="contact-panel">
      <h3 class="contact-heading">Contact Us</h3>
      <p class="contact-address">Suite 410<br>Harbourline Tower<br>820 Cordova Street<br>Vancouver, BC V6C 2R4<br>Canada</p>
      <p class="contact-phones">778-555-0142<br>778-555-0187</p>
      <p class="contact-email">info@veltanorpartners.ca</p>
      <div class="skyline-photo" role="img" aria-label="Dark photo of city office towers">
        <p class="skyline-name">VELTANOR PARTNERS</p>
        <div class="social-row">
          <span class="social-label">Follow Us on</span>
          <span class="social-square"></span>
          <span class="social-square"></span>
          <span class="social-square"></span>
          <span class="social-square"></span>
        </div>
      </div>
    </section>

    <section class="cover-panel">
      <div class="cover-top">
        <h1 class="cover-brand">VELTANOR<br>PARTNERS</h1>
      </div>
      <p class="cover-tagline">
        <span class="tagline-lead">Shaping<br>the future</span>
        <span class="tagline-tail">of your business</span>
      </p>
      <p class="cover-url">www.veltanorpartners.ca</p>
    </section>
  </main>
</body>
</html>
```